Advertisement Coaching practice

I need an advertisement (to be printed in newspaper). I have a coaching practice where I offer coaching, workshops family constellations and relationship therapy. The ad needs to express calmness, inspiration to transform but also not dull and boring. It would be great if you could use the colors from my logo into the ad.

Dimensions are: 13,04 cm Width x 9,72 cm Height.

I will add my previous self-made ad, my company logo, a portrait photo of myself and the text I want to add. Also my contact details should be visible as well.

Requirements
Nice to have
• I have updated the brief with a flyer that I had previously made by a designer. It would be a nice to have if the ad ties in with that. You can also look at my website at www.fernbrook.nu to see what colors I used there.

```html
<!DOCTYPE html>
<html lang="nl">
<head>
<meta charset="utf-8">
<title>Fernbrook – Coaching advertentie</title>
<link href="https://fonts.googleapis.com/css2?family=Barlow+Condensed:wght@400;600&family=Montserrat:wght@700;800&family=Open+Sans:wght@400&display=swap" rel="stylesheet">
<style>
  :root{
    --teal:#8dcfb4;
    --teal-dark:#6fb89b;
    --orange:#f39a20;
    --ink:#3a3a35;
    --grey-text:#555;
    --purple:#4a2a8a;
    --white:#fff;
    --photo-warm:#8a6a58;
    --photo-cool:#aeb8c8;
  }
  html,body{margin:0;padding:0;width:1200px;height:1200px;overflow:hidden;background:var(--white);}
  .ad{position:absolute;left:0;top:165px;width:1200px;height:869px;box-sizing:border-box;border:1px solid #777;overflow:hidden;background:var(--white);}
  .ad-shapes{position:absolute;inset:0;}
  .brand{position:absolute;left:595px;top:40px;display:flex;align-items:center;gap:26px;}
  .brand-mark{width:88px;height:88px;border:4px solid #777;border-radius:50%;box-sizing:border-box;}
  .brand-name{font-family:"Open Sans",sans-serif;font-weight:400;font-size:60px;color:var(--grey-text);letter-spacing:1px;}
  .accent-line{position:absolute;left:1053px;top:202px;width:147px;height:7px;background:var(--purple);}
  .headline{position:absolute;left:500px;width:600px;top:180px;margin:0;text-align:center;font-family:"Montserrat",sans-serif;font-weight:800;line-height:1;}
  .headline .lead{display:block;color:var(--white);font-size:64px;}
  .headline .sub{display:block;color:var(--ink);font-size:43px;margin-top:8px;line-height:1.05;}
  .intro{position:absolute;left:430px;width:740px;top:355px;margin:0;text-align:center;font-family:"Barlow Condensed",sans-serif;font-size:34px;line-height:1.12;color:var(--ink);}
  .offer-title{position:absolute;left:380px;width:636px;top:472px;margin:0;padding:0 0 8px 22px;box-sizing:border-box;border-bottom:5px solid var(--orange);font-family:"Montserrat",sans-serif;font-weight:700;font-size:27px;color:var(--ink);}
  .offer-list{position:absolute;left:372px;top:522px;margin:0;padding:0;list-style:none;font-family:"Barlow Condensed",sans-serif;font-size:29px;color:var(--ink);line-height:32px;white-space:nowrap;}
  .offer-list li{position:relative;padding-left:25px;}
  .offer-list li::before{content:"";position:absolute;left:2px;top:12px;width:11px;height:11px;border-radius:50%;background:var(--orange);}
  .dots{position:absolute;left:43px;top:683px;display:grid;grid-template-columns:12px 12px;column-gap:15px;row-gap:22px;}
  .dots span{width:11px;height:11px;border-radius:50%;background:var(--orange);}
  .workshops{position:absolute;left:110px;top:676px;margin:0;font-family:"Barlow Condensed",sans-serif;font-size:26px;letter-spacing:-0.2px;line-height:32px;color:var(--ink);white-space:nowrap;}
  .workshops span{display:block;}
  .contact{position:absolute;left:780px;width:420px;top:635px;height:234px;text-align:center;}
  .contact-url{position:absolute;top:12px;left:40px;width:380px;font-family:"Montserrat",sans-serif;font-weight:700;font-size:31px;color:var(--ink);}
  .contact-rule{position:absolute;left:0;right:0;height:1px;background:rgba(255,255,255,.8);}
  .contact-rule.top{top:58px;}
  .contact-rule.bottom{top:155px;}
  .contact-name{position:absolute;top:66px;left:40px;width:380px;font-family:"Open Sans",sans-serif;font-size:31px;color:var(--white);}
  .socials{position:absolute;top:108px;left:123px;display:flex;gap:17px;}
  .socials span{width:38px;height:38px;border-radius:50%;background:var(--white);}
  .phone{position:absolute;top:164px;left:46px;display:flex;align-items:center;gap:22px;}
  .phone-icon{width:50px;height:50px;border-radius:50%;background:var(--ink);display:flex;align-items:center;justify-content:center;}
  .phone-number{font-family:"Barlow Condensed",sans-serif;font-weight:600;font-size:56px;color:var(--ink);letter-spacing:-1px;}
</style>
</head>
<body>
<div class="ad">
  <svg class="ad-shapes" width="1200" height="869" viewBox="0 0 1200 869">
    <defs>
      <linearGradient id="footer-fade" x1="0" x2="1" y1="0" y2="0">
        <stop offset="0" stop-color="#c9c9c9"/>
        <stop offset="0.7" stop-color="#fafafa"/>
        <stop offset="1" stop-color="#ffffff"/>
      </linearGradient>
      <linearGradient id="band-grey" x1="0" x2="1" y1="0" y2="1">
        <stop offset="0" stop-color="#d8d8d8"/>
        <stop offset="1" stop-color="#bdbdbd"/>
      </linearGradient>
      <linearGradient id="portrait-tone" x1="0" x2="0.6" y1="0" y2="1">
        <stop offset="0" stop-color="#4a3c38"/>
        <stop offset="0.45" stop-color="#8a6a58"/>
        <stop offset="1" stop-color="#aeb8c8"/>
      </linearGradient>
    </defs>
    <rect class="footer-band" x="0" y="635" width="1200" height="234" fill="url(#footer-fade)"/>
    <rect class="teal-panel" x="240" y="167" width="960" height="468" fill="var(--teal)"/>
    <path class="teal-edge" d="M505 167 H540 L280 635 H230 Z" fill="var(--teal-dark)"/>
    <path class="portrait-frame" d="M0 0 H480 Q512 0 512 35 V130 Q512 160 497 185 L262 628 Q243 665 205 665 H0 Z" fill="url(#band-grey)"/>
    <path class="portrait" role="img" aria-label="Portretfoto van de coach, glimlachend, in een lichtblauwe blouse" d="M0 0 H450 Q480 0 480 30 V110 Q480 140 465 165 L240 600 Q220 635 185 635 H0 Z" fill="url(#portrait-tone)"/>
    <path class="contact-panel" d="M834 635 H1200 V869 H687 Z" fill="var(--orange)"/>
  </svg>

  <div class="brand">
    <div class="brand-mark"></div>
    <div class="brand-name">fernbrook</div>
  </div>
  <div class="accent-line"></div>

  <h1 class="headline">
    <span class="lead">COACHING,</span>
    <span class="sub">FAMILIEOPSTELLINGEN<br>&amp; RELATIETHERAPIE</span>
  </h1>

  <p class="intro">Trauma’s en negatieve ervaringen vormen ons en blijven nog lang voelbaar. Ze kunnen groei of geluk in de weg staan.</p>

  <h2 class="offer-title">Ik ben Mirella en ondersteun je bij het:</h2>
  <ul class="offer-list">
    <li>Doorbreken van belemmerende patronen;</li>
    <li>Beter omgaan met conflicten;</li>
    <li>In gezonde verbinding met elkaar als koppel of met anderen komen;</li>
  </ul>

  <div class="dots"><span></span><span></span><span></span><span></span><span></span><span></span><span></span><span></span><span></span><span></span></div>
  <p class="workshops">
    <span>Maandelijks geef ik workshops familieopstellingen.</span>
    <span>Ook houd ik themasessies rond adoptie, moeder-dochterdyna-</span>
    <span>miek of relaties. Ook bied ik individuele coaching, relatietherapie</span>
    <span>en retraites aan. Kijk op de website voor meer info of neem con-</span>
    <span>tact op en ontdek wat het beste bij jou past.</span>
  </p>

  <div class="contact">
    <div class="contact-url">www.fernbrook.nu</div>
    <div class="contact-rule top"></div>
    <div class="contact-name">Mirella Dastani</div>
    <div class="socials"><span></span><span></span><span></span><span></span></div>
    <div class="contact-rule bottom"></div>
    <div class="phone">
      <div class="phone-icon">
        <svg width="28" height="28" viewBox="0 0 24 24"><path d="M6.6 10.8a15.1 15.1 0 0 0 6.6 6.6l2.2-2.2a1 1 0 0 1 1-.25 11.4 11.4 0 0 0 3.6.57 1 1 0 0 1 1 1V20a1 1 0 0 1-1 1A17 17 0 0 1 3 4a1 1 0 0 1 1-1h3.5a1 1 0 0 1 1 1c0 1.250.2 2.45.57 3.6a1 1 0 0 1-.25 1z" fill="#fff"/></svg>
      </div>
      <div class="phone-number">06-12 34 56 78</div>
    </div>
  </div>
</div>
</body>
</html>
```